Harbor Sushi & Steak Dinner Menu

I'm looking for a MENU design with a particular feel. I want to have a base template made that I can then use for future alterations to the menu; ie I can go in and change out different entrees as the menu changes but the template will remain the same. (Ideally it would be in an Apple Pages format.). Also ideally - dinner menu will occupy 2 pages 8.5 x 11. The restaurant's name is Harbor. It is a MODERN steak house that will also feature Sushi, a Raw Bar, Exquisite Cocktails and a sophisticated nightlife crowd. I have attached our LOGO, a secondary logo that we will be featuring throughout the project including on the menu cover (the gold U). Finally - I have attached the content that we would like to see. AGAIN - I REITERATE: High end dining and lounge atmosphere. A couple of restaurants / menus that I love are Corvellin in NYC and Marrowby Steakhouse in Long Island NY. Please do not duplicate - just trying to offer some suggestions.

Requirements
Must have
• A sophisticated and elegant feel without being stuffy or old.

```html
<!DOCTYPE html>
<html lang="en">
<head>
<meta charset="utf-8">
<title>Harbor Sushi &amp; Steak Dinner Menu</title>
<link rel="stylesheet" href="https://fonts.googleapis.com/css2?family=Alfa+Slab+One&family=Montserrat:wght@400;600&display=swap">
<style>
  :root {
    --red: #c8283a;
    --gold: #d4bf7a;
    --gold-line: #cdb571;
    --ink: #1f1f1f;
    --muted: #3a3a3a;
    --left-bg: #ffffff;
    --right-bg: #e8e8ea;
  }
  * { margin: 0; padding: 0; box-sizing: border-box; }
  html, body { width: 1200px; height: 779px; overflow: hidden; background: #fff; }
  .menu { position: relative; width: 1200px; height: 779px; font-family: "Montserrat", sans-serif; color: var(--ink); }
  .page { position: absolute; top: 0; height: 779px; width: 600px; }
  .page--left { left: 0; background: var(--left-bg); }
  .page--right { left: 600px; background: var(--right-bg); }

  .photo { position: absolute; }
  .photo--nigiri { left: 270px; top: 0; width: 320px; height: 370px; background: radial-gradient(ellipse at 55% 50%, #f2a37c 0%, #f6d8c8 45%, #ffffff 80%); }
  .photo--platter { left: 5px; top: 392px; width: 255px; height: 110px; background: radial-gradient(ellipse at 50% 55%, #f0b090 0%, #f3e0d2 55%, #ffffff 85%); }
  .photo--rolls { left: 340px; top: 530px; width: 255px; height: 185px; background: radial-gradient(ellipse at 60% 55%, #f5b34c 0%, #f7dcae 50%, #ffffff 85%); }
  .photo--maki { left: 850px; top: 0; width: 350px; height: 235px; background: radial-gradient(ellipse at 80% 55%, #6b6b6b 0%, #d8d6d2 45%, var(--right-bg) 85%); }
  .photo--shrimp { left: 560px; top: 345px; width: 255px; height: 165px; background: radial-gradient(ellipse at 50% 50%, #ef8a5a 0%, #f3c8b0 45%, rgba(232,232,234,0) 80%); }
  .photo--seafood { left: 885px; top: 570px; width: 315px; height: 205px; background: radial-gradient(ellipse at 55% 50%, #e07a45 0%, #e9c6ad 50%, var(--right-bg) 85%); }

  .brand { position: absolute; left: 34px; top: 58px; display: flex; align-items: center; gap: 8px; }
  .brand__dot { width: 10px; height: 10px; border-radius: 50%; background: var(--gold); }
  .brand__name { font-family: "Montserrat", sans-serif; font-weight: 400; font-size: 34px; letter-spacing: 7px; color: var(--gold); }

  .section-band { position: absolute; height: 18px; width: 36px; background: var(--gold); }
  .section-rule { position: absolute; height: 1px; background: var(--gold-line); }
  .section-title { position: absolute; font-family: "Alfa Slab One", serif; font-size: 23px; line-height: 1; letter-spacing: 2.5px; color: var(--red); white-space: nowrap; }

  .item-list { position: absolute; list-style: none; font-size: 8.6px; letter-spacing: 0.6px; color: var(--muted); }
  .item-list li { position: relative; height: 15.7px; line-height: 15.7px; white-space: nowrap; }
  .item-list b { font-weight: 600; font-size: 9.6px; color: var(--ink); letter-spacing: 0.2px; }
  .bullet { position: absolute; top: 5px; width: 5px; height: 6px; background: var(--red); border-right: 2px solid var(--gold); }
  .item-list--left li .bullet { left: -23px; }
  .item-list--right { text-align: right; }
  .item-list--right li .bullet { right: -20px; }
  .item-list--plain li { padding-left: 0; }

  .platter-line { position: absolute; right: 682px; text-align: right; white-space: nowrap; }
  .platter-line b { font-weight: 600; font-size: 9.6px; }
  .platter-line span { font-size: 8.2px; color: var(--muted); }

  .note { position: absolute; font-size: 8.2px; letter-spacing: 1.1px; color: var(--muted); text-align: right; line-height: 15.7px; white-space: nowrap; }
  .platter-copy { position: absolute; left: 672px; top: 576px; font-size: 12px; letter-spacing: 0.3px; line-height: 14.5px; color: var(--muted); }
</style>
</head>
<body>
<main class="menu">
  <section class="page page--left"></section>
  <section class="page page--right"></section>

  <div class="photo photo--nigiri" role="img" aria-label="Photo of maki rolls and salmon nigiri on a white plate with chopsticks and soy sauce"></div>
  <div class="photo photo--platter" role="img" aria-label="Photo of an assorted sushi platter with wasabi and pickled ginger"></div>
  <div class="photo photo--rolls" role="img" aria-label="Photo of salmon-topped sushi rolls on a plate"></div>
  <div class="photo photo--maki" role="img" aria-label="Photo of large sushi rolls with soy sauce and chopsticks on a tray"></div>
  <div class="photo photo--shrimp" role="img" aria-label="Photo of cooked whole shrimp"></div>
  <div class="photo photo--seafood" role="img" aria-label="Photo of a seafood platter with crab, mussels, prawns, squid and lemon"></div>

  <div class="brand">
    <span class="brand__dot"></span>
    <span class="brand__name">HARBOR</span>
  </div>

  <!-- Sushi / Sashimi -->
  <div class="section-band" style="left:27px;top:173px"></div>
  <div class="section-rule" style="left:63px;top:173px;width:255px"></div>
  <h2 class="section-title" style="left:71px;top:171px">SUSHI / SASHIMI</h2>
  <ul class="item-list item-list--left" style="left:94px;top:208px">
    <li style="height:19px"><i class="bullet"></i><b>Toro;</b> blue fin tuna belly (gf) Unagi;</li>
    <li><i class="bullet"></i><b>fresh water eel</b></li>
    <li><i class="bullet"></i><b>Ebi</b>; cooked shrimp</li>
    <li><i class="bullet"></i><b>Sake</b>; salmon</li>
    <li><i class="bullet"></i><b>Hamachi</b>; yellowtail</li>
    <li><i class="bullet"></i><b>Madai</b>; red snapper</li>
    <li><i class="bullet"></i><b>Uni</b>; sea urchin</li>
    <li><i class="bullet"></i><b>Maguro</b>; tuna</li>
    <li><i class="bullet"></i><b>Hirame</b>; fluke</li>
  </ul>

  <!-- Sushi Platters -->
  <div class="section-rule" style="left:72px;top:371px;width:460px"></div>
  <h2 class="section-title" style="right:671px;top:370px">SUSHI PLATTERS</h2>
  <div class="section-band" style="left:532px;top:372px"></div>
  <div class="platter-line" style="top:414px"><b>Small:</b></div>
  <div class="platter-line" style="top:425px"><span>Five Pieces assorted sushi, nine pieces sashimi, spicy tuna roll (gf)</span></div>
  <div class="platter-line" style="top:440px"><b>Large:</b></div>
  <div class="platter-line" style="top:451px"><span>Eight Pieces assorted sushi, eighteen pieces of sashimi, alaskan roll, rainbow roll (gf)</span></div>
  <i class="bullet" style="left:526px;top:419px"></i>
  <i class="bullet" style="left:526px;top:444px"></i>

  <!-- Classic Rolls -->
  <div class="section-band" style="left:27px;top:542px"></div>
  <div class="section-rule" style="left:63px;top:542px;width:469px"></div>
  <h2 class="section-title" style="left:71px;top:540px">CLASSIC ROLLS</h2>
  <ul class="item-list item-list--left" style="left:94px;top:576px">
    <li><i class="bullet"></i><b>Yellowtail</b>; inside out roll with scallions (gf)</li>
    <li>Spicy Tuna or Salmon or Yellowtail; spicy mayo</li>
    <li><i class="bullet"></i><b>California</b>: crab meat, cucumber and avocado (gf)</li>
    <li><i class="bullet"></i><b>Vegetable</b>: avocado, cucumber, asparagus and pickled reddish (gf)</li>
    <li><i class="bullet"></i><b>Spider:</b> soft shell crab and avocado with eel sauce</li>
    <li><i class="bullet"></i><b>Shrimp Tempura:</b> deep fried tempura shrimp and eel sauce</li>
    <li>Alaskan; salmon and avocado (gf)</li>
  </ul>

  <!-- Special Rolls -->
  <div class="section-band" style="left:620px;top:95px"></div>
  <div class="section-rule" style="left:656px;top:95px;width:256px"></div>
  <h2 class="section-title" style="left:671px;top:93px">SPECIAL ROLLS</h2>
  <ul class="item-list item-list--left" style="left:707px;top:146px">
    <li><i class="bullet" style="left:-35px"></i><b>The Harbor:</b> tuna, salmon, yellowtail, avocado, spicy mayo, soy bean paper</li>
    <li><i class="bullet" style="left:-35px"></i><b>King Crab Rainbow:</b> king crab, avocado, cucumbers, assorted fish on top</li>
    <li><i class="bullet" style="left:-35px"></i><b>Empress:</b> Shrimp tempura, spicy tuna on top, eel sauce, spicy mayo</li>
    <li><i class="bullet" style="left:-35px"></i><b>Spicy Girl:</b> Spicy crunchy crab meat, cucumber, shrimp on top</li>
    <li><i class="bullet" style="left:-35px"></i><b>Dragon:</b> Eel, cucumber, avocado, and tobiko on top, eel sauce</li>
    <li><i class="bullet" style="left:-35px"></i><b>Yummy:</b> spicy crunchy salmon, avocado, mango and salmon on top</li>
    <li><i class="bullet" style="left:-35px"></i><b>No. 9:</b> Shrimp Tempura, avocado, kani, spicy mayo, tobiko</li>
    <li><i class="bullet" style="left:-35px"></i><b>Sunrise Roll:</b> spicy crunchy tuna and avocado, spicy crunchy salmon on top</li>
  </ul>

  <!-- Seafood Raw Bar -->
  <div class="section-rule" style="left:672px;top:347px;width:468px"></div>
  <h2 class="section-title" style="right:70px;top:327px">SEAFOOD RAW BAR</h2>
  <div class="section-band" style="left:1140px;top:329px"></div>
  <ul class="item-list item-list--right" style="right:90px;top:367px">
    <li><i class="bullet"></i><b>Lobster Cocktail</b></li>
    <li><i class="bullet"></i><b>Shrimp Cocktail</b></li>
    <li><i class="bullet"></i><b>Clams on the Half Shell</b></li>
    <li><i class="bullet"></i><b>Oysters on the Half Shell</b></li>
    <li><i class="bullet"></i><b>Colossal Crab Cocktail</b></li>
  </ul>
  <p class="note" style="right:90px;top:460px">Raw Bar Plate for One: Two Shrimp, Half of a One Pound Lobster,<br>Two Clams, One East Coast Oyster, One West Coast Oyster</p>

  <!-- Seafood Platters -->
  <div class="section-band" style="left:627px;top:542px"></div>
  <div class="section-rule" style="left:663px;top:542px;width:469px"></div>
  <h2 class="section-title" style="left:671px;top:540px">SEAFOOD PLATTERS</h2>
  <p class="platter-copy">Shrimp, Oysters, Clams, Lobster and Crab<br>Large or Colossal</p>
</main>
</body>
</html>
```